Design refresh of existing HR Application

QuillStaff is an HR & Payroll processing software, already in use by thousands of people. It is a feature packed, enterprise-grade software that is also simple and user friendly. Visit us at https://quillstaff.example

Seeking a refresh of the app design/UI.

Key objectives are to make it "sleeker", more professional and polished, whist still retaining functionality. Not intended to be a massive overhaul, but more of reorganization and improvements on design elements.

You may login to our demo account to see the app live.
https://app.quillstaff.example/login
User: demo@quillstaff.example
Password: Zip20

Target Market(s)

HR Managers, business administrators/owners and employees.

Industry/Entity Type

Business Software

Number of Pages Required

4 page

Font styles to use
Other font styles liked:
• Lato

Colors
0255a3
3377b5
00a990
33b8a4
f37122
faa54b

Requirements
Must have
• Must retain the current functionality on each page.
Nice to have
• Fine to suggest changes to colors, font sizes, card designs, moving sections around and any other design element changes.

```html
<!DOCTYPE html>
<html lang="en">
<head>
<meta charset="utf-8">
<title>QuillStaff – Dashboard</title>
<link href="https://fonts.googleapis.com/css2?family=Roboto:wght@400;500;700&family=Open+Sans:wght@400;600;700&display=swap" rel="stylesheet">
<style>
:root{
  --navy:#083d80;
  --side:#0b4790;
  --card:#3a7dc0;
  --card-2:#3377b5;
  --deep:#0255a3;
  --row:#0d4c9c;
  --teal:#33b8a4;
  --teal-2:#00a990;
  --mint:#6fe3d3;
  --orange:#f37122;
  --amber:#faa54b;
  --white:#ffffff;
  --soft:#cfe0f3;
}
*{box-sizing:border-box;margin:0;padding:0}
html,body{width:1200px;height:1130px;overflow:hidden}
body{background:var(--navy);font-family:"Roboto",sans-serif;color:var(--white);position:relative}
.abs{position:absolute}
/* header */
.topbar{left:0;top:0;width:1200px;height:52px}
.brand-box{left:21px;top:14px;width:53px;height:24px;background:var(--white);display:flex;align-items:center;justify-content:center;color:var(--deep);font:700 9px "Open Sans",sans-serif}
.company{left:88px;top:19px;font:700 10px "Open Sans",sans-serif;letter-spacing:.3px}
.company span{color:var(--amber);margin-left:6px;font-size:8px}
.user{right:175px;top:12px;text-align:right;font:600 10px "Open Sans",sans-serif;line-height:11px;white-space:nowrap}
.user small{display:block;color:var(--amber);font-weight:400;font-size:9px}
.avatar-top{left:1034px;top:11px;width:26px;height:26px;background:linear-gradient(#d9c9b4,#6d5a4b);border-radius:3px}
.top-tools{left:1068px;top:17px;font:400 9px "Open Sans",sans-serif;display:flex;gap:8px;align-items:center}
.top-tools .sep{width:1px;height:12px;background:var(--soft)}
.top-tools .dot{width:7px;height:7px;border-radius:50%;background:var(--amber)}
/* sidebar */
.sidebar{left:0;top:57px;width:144px;height:1073px;background:var(--side)}
.nav-item{position:absolute;left:0;width:144px;height:42px;display:flex;align-items:center;padding-left:20px;font:400 10.5px "Open Sans",sans-serif;gap:17px}
.nav-item.active{background:var(--deep);border-left:3px solid var(--orange);width:142px;padding-left:17px}
.nav-ico{width:26px;height:24px;display:block}
.powered{left:3px;top:504px;width:139px;height:80px;background:var(--deep);padding:7px 7px}
.powered .by{font:400 8px "Open Sans",sans-serif;color:var(--soft)}
.powered .name{display:flex;align-items:center;gap:6px;margin-top:10px;font:700 15px "Roboto",sans-serif}
.powered .name i{width:12px;height:12px;background:var(--teal);display:block}
.powered .legal{margin-top:10px;text-align:center;font:400 8px "Open Sans",sans-serif;color:var(--soft)}
/* cards */
.panel{background:var(--card);border-radius:10px}
.panel-title{position:absolute;left:14px;top:10px;font:500 12px "Roboto",sans-serif;letter-spacing:.2px}
.greet{left:154px;top:53px;width:1033px;height:58px;display:flex;align-items:center;padding-left:17px;font:400 18.5px "Roboto",sans-serif;color:var(--mint)}
/* today event */
.event{left:154px;top:120px;width:250px;height:163px}
.event h2{position:absolute;left:20px;top:11px;font:700 17px "Roboto",sans-serif;text-decoration:underline;text-underline-offset:3px}
.event .date{position:absolute;left:20px;top:40px;font:500 10px "Open Sans",sans-serif}
.event .times{position:absolute;left:20px;top:54px;font:700 27px/30px "Roboto",sans-serif}
.event .where{position:absolute;left:20px;top:120px;font:700 9.5px/12px "Open Sans",sans-serif}
.gauge{position:absolute;left:118px;top:22px}
/* schedule */
.schedule{left:411px;top:120px;width:524px;height:163px}
.month{position:absolute;left:302px;top:6px;border:1px solid var(--soft);border-radius:5px;font:500 8px "Roboto",sans-serif;padding:2px 6px}
.pager{position:absolute;right:12px;top:7px;color:var(--amber);font-size:11px;letter-spacing:12px}
.sched-rule{position:absolute;left:0;top:26px;width:524px;height:1px;background:rgba(255,255,255,.35)}
.sched-row{position:absolute;left:0;width:278px;height:34px;display:flex;align-items:center;font:400 8.6px "Open Sans",sans-serif;border-bottom:1px solid rgba(255,255,255,.3)}
.sched-row span{padding-left:14px}
.sched-row .c1{width:86px}
.sched-row .c2{width:105px;border-left:1px solid var(--amber);padding-left:9px;height:14px;display:flex;align-items:center}
.sched-row .c3{border-left:1px solid var(--amber);padding-left:10px;height:14px;display:flex;align-items:center}
.sched-bar{position:absolute;left:284px;top:32px;width:5px;height:122px;background:var(--soft);border-radius:3px}
.sched-bar i{display:block;height:24px;background:var(--orange);border-radius:3px}
.cal{position:absolute;left:302px;top:32px;border-collapse:collapse;width:213px;font:400 8px "Open Sans",sans-serif;text-align:center}
.cal td,.cal th{border:1px solid rgba(255,255,255,.55);height:20.5px;background:var(--deep)}
.cal th{background:#0a4a94;height:14px;font-weight:600}
.cal .we{color:var(--amber)}
.cal .mute{color:#8fb4dd}
/* time off */
.timeoff{left:944px;top:120px;width:242px;height:163px}
.tile{position:absolute;top:30px;height:94px;background:var(--deep);border-radius:4px}
.tile .art{position:absolute;left:12px;top:14px;width:30px;height:32px;border-radius:4px}
.tile .big{position:absolute;left:50px;top:25px;font:400 15px "Roboto",sans-serif}
.tile .lbl{position:absolute;left:0;width:100%;top:63px;text-align:center;font:700 9px "Roboto",sans-serif}
.request{position:absolute;left:12px;top:133px;height:21px;padding:0 9px;background:var(--orange);border-radius:11px;display:flex;align-items:center;gap:4px;font:700 8.5px "Roboto",sans-serif}
.request i{width:8px;height:8px;border:1.5px solid var(--white);border-radius:50%;display:block}
/* quick links */
.ql-title{left:158px;top:304px;font:500 12px "Roboto",sans-serif}
.ql{top:326px;height:125px;border-radius:10px;background:#3a86d4}
.ql.alt{background:#3374b8}
.ql .art{position:absolute;left:30px;top:40px;width:50px;height:45px;border-radius:6px}
.ql .num{position:absolute;top:34px;font:400 34px "Roboto",sans-serif}
.ql .cap{position:absolute;top:74px;font:500 12px "Roboto",sans-serif;display:flex;align-items:center;gap:5px;white-space:nowrap}
.ql .cap i{width:4px;height:4px;border-radius:50%;background:var(--teal);display:block}
/* tardy */
.tardy{left:154px;top:464px;width:384px;height:186px}
.t-row{position:absolute;left:12px;width:352px;height:41px;background:var(--row);border-radius:12px;display:flex;align-items:center;font:400 10px "Open Sans",sans-serif}
.t-row .pic{width:28px;height:28px;border-radius:50%;margin-left:15px;margin-right:13px;background:linear-gradient(#e8d3c0,#3c2a22)}
.t-row .n{width:118px}
.t-row .r{width:131px;border-left:1px solid var(--orange);padding-left:9px;color:var(--soft)}
.t-row .v{border-left:1px solid var(--orange);padding-left:12px}
.scroll{position:absolute;width:5px;background:var(--soft);border-radius:3px}
.scroll i{display:block;height:24px;background:var(--orange);border-radius:3px}
/* on leave */
.leave{left:548px;top:464px;width:638px;height:186px}
.chip{position:absolute;top:8px;height:21px;border-radius:11px;border:1px solid rgba(255,255,255,.3);background:#3773b4;display:flex;align-items:center;gap:5px;padding:0 9px;font:500 9.5px "Roboto",sans-serif}
.chip i{width:11px;height:10px;background:#a9c7ec;border-radius:2px;display:block}
.chip.on{background:var(--orange);border-color:var(--orange)}
.chip.on i{background:var(--amber)}
.filter{position:absolute;right:17px;top:13px;font:400 9.5px "Open Sans",sans-serif;display:flex;gap:5px;align-items:center}
.filter i{width:0;height:0;border-left:5px solid transparent;border-right:5px solid transparent;border-top:7px solid var(--white);display:block}
.leave-card{position:absolute;left:20px;top:57px;width:254px;height:88px;border:1px solid var(--teal);border-radius:10px}
.leave-card .pic{position:absolute;left:15px;top:22px;width:40px;height:40px;border-radius:50%;background:linear-gradient(#e6cdb7,#3a2820)}
.leave-card .n{position:absolute;left:71px;top:29px;font:400 11.5px "Open Sans",sans-serif}
.leave-card .r{position:absolute;left:71px;top:46px;font:400 8px "Open Sans",sans-serif}
.pill{position:absolute;left:152px;top:35px;border:1px solid var(--teal);border-radius:9px;padding:2px 12px;font:400 8px "Open Sans",sans-serif;color:#e3fbf6}
.pager-dot{position:absolute;left:316px;top:166px;width:6px;height:6px;border-radius:50%;background:var(--orange)}
/* notifications */
.notes{left:154px;top:661px;width:610px;height:259px}
.ghost{position:absolute;height:24px;border:1.5px solid var(--teal);border-radius:12px;padding:0 10px;display:flex;align-items:center;font:400 10px "Open Sans",sans-serif;color:#e3fbf6}
.n-row{position:absolute;left:15px;width:552px;height:49px;background:var(--row);border-radius:10px;display:flex;align-items:center;font:400 9.5px "Open Sans",sans-serif}
.n-ico{width:32px;height:32px;border-radius:50%;background:var(--amber);margin:0 10px;display:flex;align-items:center;justify-content:center}
.n-ico b{width:14px;height:13px;border:2px solid var(--white);border-radius:2px;display:block}
.n-act{position:absolute;right:18px;display:flex;align-items:center;gap:9px;color:#8fb8ea;font-size:10px}
.n-act .s{width:1px;height:12px;background:var(--orange)}
/* announcements */
.ann{left:775px;top:661px;width:411px;height:259px}
.a-row{position:absolute;left:10px;top:63px;width:376px;height:50px;background:var(--row);border-radius:10px;padding:7px 90px 0 15px;font:400 9.6px/13px "Open Sans",sans-serif}
.a-act{position:absolute;right:15px;top:19px;display:flex;gap:8px;align-items:center;color:#8fb8ea;font-size:10px}
.a-act .s{width:1px;height:12px;background:var(--orange)}
/* updates */
.updates{left:154px;top:930px;width:610px;height:173px}
.empty{position:absolute;left:0;width:610px;top:91px;text-align:center;font:400 9.6px "Open Sans",sans-serif}
</style>
</head>
<body>

<header class="abs topbar">
  <div class="abs brand-box">MFG</div>
  <div class="abs company">MANUFACTURING (DEMO)<span>&#8964;</span></div>
  <div class="abs user">Admin, Demo<small>HR Administrator</small></div>
  <div class="abs avatar-top" role="img" aria-label="Profile photo of the signed-in administrator"></div>
  <div class="abs top-tools"><span class="sep"></span><span>English &#8964;</span><span class="sep"></span><span>?</span><span class="sep"></span><span class="dot"></span></div>
</header>

<nav class="abs sidebar">
  <div class="nav-item active" style="top:2px"><span class="nav-ico" role="img" aria-label="Dashboard gauge icon" style="background:var(--amber);border-radius:13px 13px 3px 3px;height:14px"></span>Dashboard</div>
  <div class="nav-item" style="top:47px"><span class="nav-ico" role="img" aria-label="Employees icon" style="background:var(--soft);border-radius:10px 10px 3px 3px;height:15px"></span>Employees</div>
  <div class="nav-item" style="top:89px"><span class="nav-ico" role="img" aria-label="Calendar icon" style="background:var(--soft);border-radius:3px"></span>Calendar</div>
  <div class="nav-item" style="top:131px"><span class="nav-ico" role="img" aria-label="Expenses icon" style="background:var(--soft);border-radius:3px"></span>Expenses</div>
  <div class="nav-item" style="top:172px"><span class="nav-ico" role="img" aria-label="Payroll icon" style="background:var(--soft);border-radius:3px;height:20px"></span>Payroll</div>
  <div class="nav-item" style="top:221px"><span class="nav-ico" role="img" aria-label="Loans money bag icon" style="background:var(--soft);border-radius:50% 50% 40% 40%"></span>Loans</div>
  <div class="nav-item" style="top:259px"><span class="nav-ico" role="img" aria-label="Performance rocket icon" style="background:var(--soft);border-radius:3px 12px 3px 12px"></span>Performance</div>
  <div class="nav-item" style="top:302px"><span class="nav-ico" role="img" aria-label="Engagement megaphone icon" style="background:var(--soft);border-radius:50%"></span>Engagement</div>
  <div class="nav-item" style="top:343px"><span class="nav-ico" role="img" aria-label="Reports icon" style="background:var(--soft);border-radius:3px"></span>Reports</div>
  <div class="nav-item" style="top:386px"><span class="nav-ico" role="img" aria-label="Settings gear icon" style="background:var(--soft);border-radius:50%"></span>Settings</div>
</nav>
<div class="abs powered">
  <div class="by">Powered by</div>
  <div class="name"><i></i>QuillStaff</div>
  <div class="legal">Terms | Privacy</div>
</div>

<section class="abs panel greet">Good morning employee 110023. It’s great to see you!</section>

<section class="abs panel event">
  <h2>TODAY’S EVENT</h2>
  <div class="date">MON, 01 JUN 20</div>
  <div class="times">09:00<br>18:00</div>
  <div class="where">WORKING<br>BRANCH B</div>
  <svg class="gauge" width="125" height="125" viewBox="0 0 125 125">
    <circle cx="61" cy="62" r="54" fill="none" stroke="var(--amber)" stroke-width="8" stroke-dasharray="170 400" transform="rotate(90 61 62)"/>
    <circle cx="61" cy="62" r="54" fill="none" stroke="var(--orange)" stroke-width="9" stroke-dasharray="175 400" transform="rotate(-90 61 62)"/>
    <text x="61" y="50" text-anchor="middle" fill="#fff" font-family="Open Sans,sans-serif" font-weight="700" font-size="9">CHECKED IN</text>
    <text x="61" y="78" text-anchor="middle" fill="#fff" font-family="Roboto,sans-serif" font-size="24">08:50</text>
  </svg>
</section>

<section class="abs panel schedule">
  <div class="panel-title">MY SCHEDULE</div>
  <div class="month">JUNE</div>
  <div class="pager">‹›</div>
  <div class="sched-rule"></div>
  <div class="sched-row" style="top:29px"><span class="c1">Mon &nbsp;- &nbsp;JUN &nbsp;01</span><span class="c2">09:00 Working</span><span class="c3">18:00 Branch B</span></div>
  <div class="sched-row" style="top:63px"><span class="c1">Tue &nbsp;- &nbsp;JUN &nbsp;02</span><span class="c2">09:00 Working</span><span class="c3">18:00 Branch B</span></div>
  <div class="sched-row" style="top:97px"><span class="c1">Thu &nbsp;- &nbsp;JUN &nbsp;04</span><span class="c2">10:00 Work (Project A)</span><span class="c3">12:00 Branch A</span></div>
  <div class="sched-row" style="top:131px;border-bottom:0"><span class="c1">Thu &nbsp;- &nbsp;JUN &nbsp;04</span><span class="c2">10:00 Work (Project A)</span><span class="c3">12:00 Branch A</span></div>
  <div class="sched-bar"><i></i></div>
  <table class="cal">
    <tr><th>M</th><th>T</th><th>W</th><th>T</th><th>F</th><th>S</th><th>S</th></tr>
    <tr><td>1</td><td>2</td><td>3</td><td>4</td><td>5</td><td class="we">6</td><td class="we">7</td></tr>
    <tr><td>8</td><td>9</td><td>10</td><td>11</td><td>12</td><td class="we">13</td><td class="we">14</td></tr>
    <tr><td>15</td><td>16</td><td>17</td><td>18</td><td>19</td><td class="we">20</td><td class="we">21</td></tr>
    <tr><td>22</td><td>23</td><td>24</td><td>25</td><td>26</td><td class="we">27</td><td class="we">28</td></tr>
    <tr><td>29</td><td>30</td><td class="mute">1</td><td class="mute">2</td><td class="mute">3</td><td class="mute">4</td><td class="mute">5</td></tr>
  </table>
</section>

<section class="abs panel timeoff">
  <div class="panel-title">MY TIME OFF</div>
  <div class="tile" style="left:11px;width:107px">
    <div class="art" role="img" aria-label="Illustration of travel luggage" style="background:linear-gradient(#f06aa0,#c8437a)"></div>
    <div class="big">7 Left</div><div class="lbl">ANNUAL LEAVE</div>
  </div>
  <div class="tile" style="left:124px;width:109px">
    <div class="art" role="img" aria-label="Illustration of a medicine bottle" style="background:linear-gradient(#9fd8f5,#4b9be0)"></div>
    <div class="big">1 Taken</div><div class="lbl">SICK DAYS</div>
  </div>
  <div class="request"><i></i>REQUEST</div>
</section>

<div class="abs ql-title">QUICK LINKS</div>
<section class="abs ql" style="left:154px;width:250px">
  <div class="art" role="img" aria-label="Illustration of a calendar with a pencil" style="background:linear-gradient(#f3f6fb,#cfd9e6)"></div>
  <div class="num" style="left:102px">12</div>
  <div class="cap" style="left:96px"><i></i>EVENT AMENDMENT</div>
</section>
<section class="abs ql alt" style="left:417px;width:248px">
  <div class="art" role="img" aria-label="Illustration of a tent among trees" style="background:linear-gradient(#6fcf6a,#f3a72c)"></div>
  <div class="num" style="left:107px">02</div>
  <div class="cap" style="left:97px"><i></i>LEAVE REQUESTS</div>
</section>
<section class="abs ql" style="left:678px;width:250px">
  <div class="art" role="img" aria-label="Illustration of a clock over a bar chart" style="background:linear-gradient(#e8edf3,#f37122)"></div>
  <div class="num" style="left:110px">07</div>
  <div class="cap" style="left:101px"><i></i>EVENT REQUESTS</div>
</section>
<section class="abs ql" style="left:938px;width:248px">
  <div class="art" role="img" aria-label="Illustration of a phone with a coin" style="background:linear-gradient(#bfe4fb,#f5b52e)"></div>
  <div class="num" style="left:86px">02</div>
  <div class="cap" style="left:79px"><i></i>PAYROLLS PENDING</div>
</section>

<section class="abs panel tardy">
  <div class="panel-title" style="left:15px;top:15px">TARDY TODAY</div>
  <div class="t-row" style="top:36px"><span class="pic" role="img" aria-label="Employee photo"></span><span class="n">100 Employee</span><span class="r">HR Administrator</span><span class="v">8.0</span></div>
  <div class="t-row" style="top:82px"><span class="pic" role="img" aria-label="Employee photo"></span><span class="n">Employee</span><span class="r">HR Administrator</span><span class="v">9.0</span></div>
  <div class="t-row" style="top:128px"><span class="pic" role="img" aria-label="Employee photo"></span><span class="n">Employee 19</span><span class="r">Line Manager</span><span class="v">9.0</span></div>
  <div class="scroll" style="left:370px;top:40px;height:122px"><i></i></div>
</section>

<section class="abs panel leave">
  <div class="panel-title" style="left:20px;top:15px">WHO’S ON LEAVE TODAY</div>
  <div class="chip on" style="left:181px"><i></i>Same Department</div>
  <div class="chip" style="left:307px"><i></i>Same Branch</div>
  <div class="chip" style="left:410px"><i></i>Subordinates</div>
  <div class="filter"><i></i>Filter</div>
  <div class="leave-card">
    <div class="pic" role="img" aria-label="Employee photo"></div>
    <div class="n">34, Employee</div>
    <div class="r">HR Administrator</div>
    <div class="pill">Maternity Leave</div>
  </div>
  <div class="pager-dot"></div>
</section>

<section class="abs panel notes">
  <div class="panel-title" style="left:18px;top:13px">NOTIFICATIONS</div>
  <div class="ghost" style="left:486px;top:3px">View Starred</div>
  <div class="n-row" style="top:39px"><span class="n-ico"><b></b></span>Wijaya, Laras has remotely checked in for Working on 20/05/2020 02:07<span class="n-act" style="color:#cfe0f3;font-size:14px">‹</span></div>
  <div class="n-row" style="top:93px"><span class="n-ico"><b></b></span>Wijaya, Laras requests amendment on 15 Apr 2020 from 09:00 - 18:00<span class="n-act">★<span class="s"></span>✔<span class="s"></span>✖</span></div>
  <div class="n-row" style="top:147px"><span class="n-ico"><b></b></span>Overtime request for Wijaya, Laras - 18 May 2020 at 19:00 | 21:00 Branch A<span class="n-act">★<span class="s"></span>✔<span class="s"></span>✖</span></div>
  <div class="n-row" style="top:201px"><span class="n-ico"><b></b></span>Wijaya, Laras requests Sick Leave on 19 May 2020.<span class="n-act">★<span class="s"></span>✔<span class="s"></span>✖</span></div>
  <div class="scroll" style="left:590px;top:45px;height:197px"><i></i></div>
</section>

<section class="abs panel ann">
  <div class="panel-title" style="left:20px;top:14px">ANNOUNCEMENTS</div>
  <div class="ghost" style="left:306px;top:12px">View Starred</div>
  <div class="a-row">Free Friday drinks are available in the pantry on every week until the end of this year. Take the opportunity to get to know more people!<span class="a-act">★<span class="s"></span>✖</span></div>
  <div class="scroll" style="left:396px;top:53px;height:185px;background:#cfe0f3"></div>
</section>

<section class="abs panel updates">
  <div class="panel-title" style="left:18px;top:18px">EMPLOYEE UPDATES</div>
  <div class="ghost" style="left:502px;top:12px">View Starred</div>
  <div class="empty">There are no Announcements</div>
  <div class="scroll" style="left:594px;top:50px;height:112px"></div>
</section>

</body>
</html>
```